Zelmiroo Pop Up design for zelmiroo.com website to collect customer data

I want a pop up designed for my site zelmiroo.com. It is for signup to the site itself. I want to give my users some value in order to sign up. I want this to have graphics and to collect their full name, email address, country they are from. It must say Sign up today and receive all these items for free, A $129 Value, 1. Zelmiroo Custom Travel tools on Web App, The Ebook Packing Light for Long Journeys, and the Golden Route Planner Sheets!

I want this to look exciting so people actually sign up.
I want to be able to put this on facebook and add to my wordpress website.
I want it to match my current website
I currently use ninja forms on my site

Once designed this also needs to be coded for my site.
You can get my color scheme right on the site. I want this to pop

thanks

Industry/Entity Type

Travel

Font styles to use
Serif
Sans Serif

Colors
33a6d7
9bcb3c
ffffff

Requirements
Must have
• A graphic of the ebook, an arrow rounded or something bringing attention to the free items. A sign up point asking for first name, last name, email. I use ninja forms and mailchimp. this will be a pop up within all of my blogs and every page of my site, also country

```html
<!DOCTYPE html>
<html lang="en">
<head>
<meta charset="utf-8">
<title>Zelmiroo Sign Up Pop Up</title>
<link rel="stylesheet" href="https://fonts.googleapis.com/css2?family=Oswald:wght@600;700&family=Montserrat:wght@200;300;400;500;600;700;800&display=swap">
<style>
  :root{
    --brand-blue:#33a6d7;
    --brand-blue-deep:#1e8fd0;
    --brand-green:#9bcb3c;
    --brand-green-light:#a6d346;
    --ink:#3a3a3a;
    --ink-soft:#555;
    --white:#ffffff;
    --stage:#e9e9e9;
    --field-text:#9c9c9c;
    --teal:#13919a;
  }
  *{box-sizing:border-box;margin:0;padding:0}
  html,body{width:1200px;height:1200px;overflow:hidden}
  body{background:var(--stage);font-family:"Montserrat",Arial,sans-serif;color:var(--ink)}

  .popup{position:absolute;left:30px;top:332px;width:1140px;height:535px;display:flex;
    box-shadow:0 4px 14px rgba(0,0,0,.18);background:var(--white)}

  .offer{position:relative;width:702px;height:100%;background:linear-gradient(120deg,#fff 40%,#f1f1f1 100%);overflow:hidden}
  .offer__headline{position:absolute;right:44px;top:48px;font-family:"Oswald",Impact,sans-serif;font-weight:700;
    font-size:86px;line-height:1;letter-spacing:-1px;color:var(--brand-blue);text-transform:uppercase;
    text-shadow:0 2px 0 rgba(0,0,0,.08)}
  .offer__sub{position:absolute;right:44px;top:160px;font-size:31px;font-weight:500;color:var(--ink);white-space:nowrap}
  .offer__value{position:absolute;right:44px;top:206px;font-size:35px;font-weight:700;color:var(--ink);white-space:nowrap}
  .offer__value .accent{color:var(--brand-green)}

  .benefits{position:absolute;left:0;top:0;width:100%;height:100%}
  .benefit{position:absolute;display:flex;align-items:center;gap:10px;border-bottom:1.5px solid var(--brand-blue);padding-bottom:6px}
  .benefit__icon{width:30px;height:34px;flex:none}
  .benefit__text{font-size:16px;font-weight:500;line-height:1.15;color:var(--ink-soft)}
  .benefit--app{left:162px;top:296px;width:260px}
  .benefit--ebook{left:133px;top:368px;width:289px}
  .benefit--sheets{left:104px;top:436px;width:318px}

  .sheet{position:absolute;left:424px;top:286px;width:118px;height:210px;background:var(--white);
    box-shadow:0 2px 6px rgba(0,0,0,.25);padding:8px 6px;transform:rotate(2deg)}
  .sheet__title{font-size:9px;font-weight:700;color:var(--teal);text-align:center;margin-bottom:4px}
  .sheet__band{background:var(--teal);color:#fff;font-size:4.5px;padding:1px 3px;margin:3px 0 2px}
  .sheet__items{display:grid;grid-template-columns:1fr 1fr;gap:2px 4px}
  .sheet__item{font-size:4.5px;color:#555;display:flex;align-items:center;gap:2px}
  .sheet__item::before{content:"";width:4px;height:4px;border:.5px solid #777;flex:none}

  .ebook{position:absolute;left:543px;top:280px;width:124px;height:214px;
    background:linear-gradient(180deg,#2a1a14 0%,#5a3120 45%,#c96a25 62%,#6b3a1c 80%,#2a1a12 100%);
    box-shadow:4px 3px 8px rgba(0,0,0,.35);border-right:3px solid #3b1f16}
  .ebook__title{position:absolute;left:12px;top:34px;right:8px;font-size:9.5px;color:#fff;line-height:1.25;transform:rotate(-3deg)}
  .ebook__title strong{display:block;color:#f7c21b;font-weight:800;font-size:10.5px;text-transform:uppercase}

  .signup{position:relative;width:438px;height:100%;
    background:radial-gradient(ellipse at 70% 40%,var(--brand-green-light) 0%,var(--brand-green) 70%);
    display:flex;flex-direction:column;align-items:center;padding-top:50px}
  .signup__title{text-align:center;color:var(--white);text-shadow:1px 2px 3px rgba(0,0,0,.3);text-transform:uppercase;line-height:1}
  .signup__title .thin{display:block;font-weight:300;font-size:64px;letter-spacing:2px}
  .signup__title .bold{display:block;font-weight:700;font-size:66px;margin-top:14px}
  .signup__form{margin-top:26px;display:flex;flex-direction:column;gap:14px;width:380px}
  .field{height:50px;border-radius:25px;background:var(--white);border:2px solid #dfe9cf;display:flex;align-items:center;
    padding:0 18px;gap:10px;font-size:16px;color:var(--field-text)}
  .field svg{width:18px;height:18px;flex:none}
  .signup__button{margin:36px auto 0;width:142px;height:31px;border-radius:16px;border:2px solid #8ed0f0;
    background:linear-gradient(180deg,#3fb3ea,var(--brand-blue-deep));color:var(--white);
    font-family:inherit;font-size:17px;font-weight:500}
</style>
</head>
<body>
<main class="popup">
  <section class="offer">
    <h1 class="offer__headline">Sign up today</h1>
    <p class="offer__sub">and receive all these items</p>
    <p class="offer__value">FOR <span class="accent">FREE</span>, A <span class="accent">$129</span> VALUE</p>

    <ul class="benefits">
      <li class="benefit benefit--app">
        <svg class="benefit__icon" viewBox="0 0 30 34"><rect x="6" y="2" width="18" height="30" rx="3" fill="none" stroke="#33a6d7" stroke-width="2"/><rect x="10" y="10" width="10" height="10" rx="2" fill="#33a6d7"/><circle cx="15" cy="28" r="1.5" fill="#33a6d7"/></svg>
        <span class="benefit__text">Zelmiroo Custom<br>Travel tools on Web App</span>
      </li>
      <li class="benefit benefit--ebook">
        <svg class="benefit__icon" viewBox="0 0 30 34"><rect x="3" y="3" width="22" height="28" fill="none" stroke="#33a6d7" stroke-width="2"/><path d="M7 12h10M7 17h10M7 22h8" stroke="#33a6d7" stroke-width="2"/><circle cx="23" cy="24" r="5" fill="#fff" stroke="#33a6d7" stroke-width="2"/></svg>
        <span class="benefit__text">The Ebook Packing Light<br>for Long Journeys</span>
      </li>
      <li class="benefit benefit--sheets">
        <svg class="benefit__icon" viewBox="0 0 30 34"><rect x="3" y="5" width="22" height="27" rx="2" fill="none" stroke="#33a6d7" stroke-width="2"/><rect x="10" y="2" width="8" height="5" fill="#33a6d7"/><path d="M7 14l2 2 3-4M7 23l2 2 3-4M15 15h7M15 24h7" stroke="#33a6d7" stroke-width="2" fill="none"/></svg>
        <span class="benefit__text">The Golden Route<br>Planner Sheets!</span>
      </li>
    </ul>

    <div class="sheet">
      <p class="sheet__title">Golden Route Planner!</p>
      <p class="sheet__band">PAPERS</p>
      <div class="sheet__items"><span class="sheet__item">Passport</span><span class="sheet__item">Insurance</span><span class="sheet__item">Visa</span><span class="sheet__item">Tickets</span></div>
      <p class="sheet__band">FUNDS</p>
      <div class="sheet__items"><span class="sheet__item">Cash</span><span class="sheet__item">Cards</span></div>
      <p class="sheet__band">MEETING</p>
      <div class="sheet__items"><span class="sheet__item">Notepad</span><span class="sheet__item">Pen</span></div>
      <p class="sheet__band">TECH</p>
      <div class="sheet__items"><span class="sheet__item">Phone</span><span class="sheet__item">Charger</span><span class="sheet__item">Adapter</span><span class="sheet__item">Headphones</span></div>
    </div>

    <div class="ebook" role="img" aria-label="Ebook cover: two hikers resting on a mountain top at sunset">
      <p class="ebook__title">The ultimate guide on<strong>Packing Light</strong>for long journeys</p>
    </div>
  </section>

  <section class="signup">
    <h2 class="signup__title"><span class="thin">Sign up</span><span class="bold">Now!</span></h2>
    <form class="signup__form">
      <label class="field"><svg viewBox="0 0 18 18"><circle cx="9" cy="5" r="4" fill="#c4c4c4"/><path d="M1 18c0-5 3.5-7 8-7s8 2 8 7z" fill="#c4c4c4"/></svg>Your Name</label>
      <label class="field"><svg viewBox="0 0 18 18"><rect x="1" y="4" width="16" height="11" rx="1" fill="none" stroke="#c4c4c4" stroke-width="1.6"/><path d="M1 5l8 6 8-6" fill="none" stroke="#c4c4c4" stroke-width="1.6"/></svg>Your Email</label>
      <label class="field"><svg viewBox="0 0 18 18"><circle cx="9" cy="9" r="7.5" fill="none" stroke="#c4c4c4" stroke-width="1.6"/><path d="M1.5 9h15M9 1.5c3 3 3 12 0 15M9 1.5c-3 3-3 12 0 15" fill="none" stroke="#c4c4c4" stroke-width="1.2"/></svg>Your Country</label>
      <button class="signup__button" type="button">Signup Now</button>
    </form>
  </section>
</main>
</body>
</html>
```